Varoden Imports Busisness cards and logo

Varoden imports is a brand new wholesale company located in Londonderry, New Hampshire dedicated to finding unique products from around the world.
Licensed to sell wine and spirits in the state and also authorized distributors of Blue Pepper Design, a manufacturer of girls and women shoes. Other products that we are currently trying to import are cheese and frozen food from Spain.
We would like a design that portraits our diversity of products and wholesale capabilities
Updates

Industry/Entity Type

It Company

```html
<!DOCTYPE html>
<html lang="en">
<head>
<meta charset="utf-8">
<title>Varoden Imports – Business Card</title>
<link rel="stylesheet" href="https://fonts.googleapis.com/css2?family=Open+Sans:wght@400;700&display=swap">
<style>
  :root {
    --bg: #e9e6e0;
    --card: #ffffff;
    --green-dark: #0f6417;
    --green-mid: #2b8a33;
    --green-lime: #7fbc1e;
    --green-pale: #d3e7b4;
    --ink: #3b3b3b;
  }
  html, body { margin: 0; padding: 0; }
  body {
    width: 1200px; height: 1020px; overflow: hidden;
    background: var(--bg);
    display: flex; align-items: center; justify-content: center;
    font-family: "Open Sans", Arial, sans-serif;
  }
  .business-card {
    position: relative;
    width: 1000px; height: 570px;
    background: var(--card);
    box-shadow: 0 14px 40px rgba(0,0,0,.22);
    overflow: hidden;
  }
  .card-art { position: absolute; inset: 0; width: 1000px; height: 570px; }
  .holder { position: absolute; left: 70px; top: 250px; color: #fff; }
  .holder-name { margin: 0; font-weight: 700; font-size: 38px; letter-spacing: .5px; line-height: 1.1; }
  .holder-title { margin: 4px 0 0; font-size: 22px; font-weight: 400; letter-spacing: .5px; }
  .brand {
    position: absolute; left: 560px; top: 175px;
    display: flex; align-items: center; gap: 16px;
  }
  .brand-dot { width: 56px; height: 56px; border-radius: 50%; background: var(--green-lime); flex: none; }
  .brand-name { margin: 0; font-weight: 700; font-size: 40px; color: var(--green-dark); white-space: nowrap; }
  .contact-list { position: absolute; left: 60px; top: 405px; margin: 0; padding: 0; list-style: none; }
  .contact-item { display: flex; align-items: center; gap: 18px; height: 38px; font-size: 17px; color: var(--ink); }
  .contact-icon {
    width: 26px; height: 26px; background: var(--green-dark);
    display: flex; align-items: center; justify-content: center; flex: none;
  }
  .contact-icon svg { width: 12px; height: 12px; }
</style>
</head>
<body>
  <article class="business-card">
    <svg class="card-art" viewBox="0 0 1000 570" role="img" aria-label="Decorative green curved band with soft pale green wash">
      <defs>
        <linearGradient id="paleWash" x1="0" y1="0" x2="1" y2="0">
          <stop offset="0.55" stop-color="#ffffff"/>
          <stop offset="1" stop-color="var(--green-pale)"/>
        </linearGradient>
        <linearGradient id="greenField" x1="0" y1="0" x2="1" y2="1">
          <stop offset="0" stop-color="var(--green-mid)"/>
          <stop offset="1" stop-color="var(--green-dark)"/>
        </linearGradient>
      </defs>
      <rect class="pale-wash" width="1000" height="570" fill="url(#paleWash)"/>
      <path class="green-band" d="M0 0 H640 C560 120 560 340 0 380 Z" fill="url(#greenField)"/>
    </svg>

    <div class="holder">
      <h1 class="holder-name">MARCUS HALE</h1>
      <p class="holder-title">GENERAL MANAGER</p>
    </div>

    <div class="brand">
      <span class="brand-dot"></span>
      <p class="brand-name">Varoden Imports</p>
    </div>

    <ul class="contact-list">
      <li class="contact-item">
        <span class="contact-icon"><svg viewBox="0 0 12 12"><path d="M3 1 L5 3 L4 5 Q5 7 7 8 L9 7 L11 9 L9 11 Q2 10 1 3 Z" fill="#fff"/></svg></span>
        014 562 3870
      </li>
      <li class="contact-item">
        <span class="contact-icon"><svg viewBox="0 0 12 12"><rect x="1" y="3" width="10" height="7" fill="none" stroke="#fff" stroke-width="1.4"/><path d="M1 3 L6 7 L11 3" fill="none" stroke="#fff" stroke-width="1.4"/></svg></span>
        sales@varoden.com
      </li>
      <li class="contact-item">
        <span class="contact-icon"><svg viewBox="0 0 12 12"><circle cx="6" cy="6" r="4.5" fill="none" stroke="#fff" stroke-width="1.4"/><path d="M1.5 6 H10.5 M6 1.5 V10.5" stroke="#fff" stroke-width="1"/></svg></span>
        www.varoden.com
      </li>
      <li class="contact-item">
        <span class="contact-icon"><svg viewBox="0 0 12 12"><path d="M6 11 C3 7 2.5 5.5 2.5 4.5 A3.5 3.5 0 0 1 9.5 4.5 C9.5 5.5 9 7 6 11 Z" fill="#fff"/><circle cx="6" cy="4.5" r="1.3" fill="var(--green-dark)"/></svg></span>
        22 Harbor Road, Suite 4, Londonderry NH
      </li>
    </ul>
  </article>
</body>
</html>
```